Velmora Bloom

I need a label design for a cbd cosmetic line. My whole idea is to base it off crystals. amethyst for acne, rose quartz for smooth skin/moisturizer, crystal quartz (glittery) for glowing skin; I would like it girly, but in a classic way, not a childish way. I wanted to base the labels off the corresponding colors of each crystal. The label size with be roughly 6.25 x 1in.

```html
<!DOCTYPE html>
<html lang="en">
<head>
<meta charset="utf-8">
<title>Velmora Bloom – cbd cosmetics label</title>
<link rel="stylesheet" href="https://fonts.googleapis.com/css2?family=Quicksand:wght@300;400&display=swap">
<style>
  :root {
    --edge-grey-light: #eeeeee;
    --edge-grey-mid: #d6d3d4;
    --edge-grey-dark: #c4c0c2;
    --rose-line: #c9a3ad;
    --panel-pale: #f6eef0;
    --panel-blush: #eedfe3;
    --bokeh-rose: #e9c9d1;
    --bokeh-deep: #c9a1ad;
    --bokeh-light: #f8e6ea;
    --magenta: #d43aa6;
  }

  html, body {
    margin: 0;
    padding: 0;
    width: 1200px;
    height: 192px;
    overflow: hidden;
    background: #ffffff;
  }

  .label {
    position: relative;
    width: 1200px;
    height: 192px;
    overflow: hidden;
    font-family: "Quicksand", sans-serif;
  }

  .edge-texture {
    position: absolute;
    top: 0;
    height: 192px;
    background: linear-gradient(160deg, var(--edge-grey-light) 0%, var(--edge-grey-mid) 45%, var(--edge-grey-light) 70%, var(--edge-grey-dark) 100%);
  }
  .edge-texture--left { left: 0; width: 84px; }
  .edge-texture--right { right: 0; width: 136px; }

  .edge-rule {
    position: absolute;
    top: 0;
    width: 2px;
    height: 192px;
    background: var(--rose-line);
    opacity: 0.7;
  }
  .edge-rule--left { left: 40px; }
  .edge-rule--right { left: 1160px; }

  .panel-pale {
    position: absolute;
    left: 84px;
    top: 0;
    width: 468px;
    height: 192px;
    background: linear-gradient(90deg, var(--panel-blush) 0%, var(--panel-pale) 40%, #faf5f6 100%);
  }

  .panel-bokeh {
    position: absolute;
    left: 552px;
    top: 0;
    width: 512px;
    height: 192px;
    background:
      radial-gradient(circle at 25% 20%, var(--bokeh-light) 0%, transparent 35%),
      radial-gradient(circle at 80% 85%, var(--bokeh-light) 0%, transparent 30%),
      linear-gradient(90deg, var(--bokeh-rose) 0%, var(--bokeh-deep) 70%, var(--bokeh-rose) 100%);
  }

  .brand-mark {
    position: absolute;
    left: 386px;
    top: 36px;
  }

  .brand-name {
    position: absolute;
    left: 586px;
    top: 22px;
    margin: 0;
    font-weight: 300;
    font-size: 56px;
    line-height: 56px;
    letter-spacing: 1px;
    text-transform: uppercase;
    color: var(--magenta);
  }

  .tagline {
    position: absolute;
    left: 588px;
    top: 136px;
    margin: 0;
    font-weight: 400;
    font-size: 30px;
    line-height: 34px;
    color: var(--magenta);
  }
</style>
</head>
<body>
  <main class="label">
    <div class="edge-texture edge-texture--left" role="img" aria-label="Faceted grey low-poly crystal texture"></div>
    <div class="edge-rule edge-rule--left"></div>

    <div class="panel-pale" role="img" aria-label="Soft pale pink faceted background"></div>
    <div class="panel-bokeh" role="img" aria-label="Glittering rose-pink bokeh sparkle background"></div>

    <div class="edge-texture edge-texture--right" role="img" aria-label="Faceted grey low-poly crystal texture"></div>
    <div class="edge-rule edge-rule--right"></div>

    <svg class="brand-mark" width="120" height="120" viewBox="0 0 120 120" aria-hidden="true">
      <circle cx="60" cy="60" r="58" fill="none" stroke="var(--magenta)" stroke-width="1.5"/>
    </svg>

    <h1 class="brand-name">Velmora<br>Bloom</h1>
    <p class="tagline">cbd cosmetics</p>
  </main>
</body>
</html>
```